Body therapist needs a business card

I need a card for my business which is teaching trainings in body therapy, the company is called Wexcombe Educational Group. I teach to massage therapists around Australia, South East Asia and the USA. I am attaching my logo which will guide you as to what colours I would like to have you consider. Please consult my website to find out more about what I do. www.corvantela.com.au

My name is Daniel Wexcombe. My phone number is (03) 9417 2608 or 0461753208. email is info@corvantela.com.au

```html
<!DOCTYPE html>
<html lang="en">
<head>
<meta charset="utf-8">
<title>Wexcombe Educational Group – Business Card</title>
<link href="https://fonts.googleapis.com/css2?family=Open+Sans:wght@400;600&family=Arimo:wght@400;700&display=swap" rel="stylesheet">
<style>
  :root {
    --backdrop: #2f343b;
    --brown: #5c3321;
    --red: #b3202a;
    --lime: #cddf2c;
    --white: #ffffff;
    --ink: #3a3a3a;
  }
  * { box-sizing: border-box; margin: 0; padding: 0; }
  html, body {
    width: 1200px; height: 1000px; overflow: hidden;
    background: var(--backdrop);
  }
  .stage {
    width: 1200px; height: 1000px;
    display: flex; flex-direction: column; align-items: center; justify-content: center;
    gap: 60px;
  }
  .card {
    position: relative;
    width: 700px; height: 400px;
    border-radius: 24px;
    overflow: hidden;
  }
  .card--front {
    background: var(--brown);
    display: flex; align-items: center; justify-content: center;
  }
  .brand { display: flex; align-items: center; gap: 22px; }
  .brand__mark { border-radius: 50%; flex: none; }
  .brand__name {
    font-family: "Open Sans", sans-serif; font-weight: 400; line-height: 1.05;
  }
  .card--front .brand__mark { width: 120px; height: 120px; background: var(--white); }
  .card--front .brand__name { color: var(--white); font-size: 44px; }
  .brand__name small { display: block; font-size: 0.46em; margin-top: 4px; }

  .card--back { background: var(--white); }
  .card--back .brand { position: absolute; left: 44px; top: 44px; gap: 16px; }
  .card--back .brand__mark { width: 76px; height: 76px; background: var(--brown); }
  .card--back .brand__name { color: var(--brown); font-size: 30px; }

  .person {
    position: absolute; right: 58px; top: 170px; text-align: right;
    font-family: "Arimo", sans-serif;
  }
  .person__name { font-size: 22px; font-weight: 700; color: var(--brown); }
  .person__name span { color: var(--red); }
  .person__role { font-size: 15px; color: var(--ink); margin-top: 2px; }

  .divider {
    position: absolute; left: 60px; right: 58px; top: 234px; height: 1px;
    background: linear-gradient(to right, rgba(179,32,42,0), var(--red));
  }

  .contacts {
    position: absolute; right: 58px; top: 246px; list-style: none;
    font-family: "Open Sans", sans-serif; font-size: 15px; color: var(--ink);
    text-align: right;
  }
  .contacts li { display: flex; align-items: center; justify-content: flex-end; gap: 8px; height: 22px; }
  .contacts svg { width: 13px; height: 13px; fill: var(--brown); flex: none; }

  .wave { position: absolute; left: 0; bottom: 0; width: 700px; height: 400px; pointer-events: none; }
</style>
</head>
<body>
<main class="stage">
  <section class="card card--front" aria-label="Card front">
    <div class="brand">
      <span class="brand__mark"></span>
      <p class="brand__name">Wexcombe<small>Educational Group</small></p>
    </div>
  </section>

  <section class="card card--back" aria-label="Card back">
    <svg class="wave" viewBox="0 0 700 400" aria-hidden="true">
      <path d="M0,272 C190,268 320,318 450,362 C540,392 620,390 700,378 L700,400 L0,400 Z" fill="var(--brown)"/>
      <path d="M0,272 C190,268 320,318 450,362 C540,392 620,390 700,378" fill="none" stroke="var(--red)" stroke-width="7"/>
      <path d="M150,278 C260,292 350,326 460,356 C545,380 625,378 700,368" fill="none" stroke="var(--lime)" stroke-width="4"/>
    </svg>

    <div class="brand">
      <span class="brand__mark"></span>
      <p class="brand__name">Wexcombe<small>Educational Group</small></p>
    </div>

    <div class="person">
      <p class="person__name">Rafael <span>Tendra</span></p>
      <p class="person__role">Senior Partner</p>
    </div>

    <div class="divider"></div>

    <ul class="contacts">
      <li>(03) 9417 2608
        <svg viewBox="0 0 24 24" aria-hidden="true"><path d="M6.6 10.8a15 15 0 0 0 6.6 6.6l2.2-2.2a1 1 0 0 1 1-.25 11.4 11.4 0 0 0 3.6.57 1 1 0 0 1 1 1V20a1 1 0 0 1-1 1A17 17 0 0 1 3 4a1 1 0 0 1 1-1h3.5a1 1 0 0 1 1 1c0 1.25.2 2.45.57 3.6a1 1 0 0 1-.25 1z"/></svg></li>
      <li>0461753208
        <svg viewBox="0 0 24 24" aria-hidden="true"><path d="M7 1h10a2 2 0 0 1 2 2v18a2 2 0 0 1-2 2H7a2 2 0 0 1-2-2V3a2 2 0 0 1 2-2zm0 3v14h10V4zm5 15.5a1 1 0 1 0 0 2 1 1 0 0 0 0-2z"/></svg></li>
      <li>info@corvantela.com.au
        <svg viewBox="0 0 24 24" aria-hidden="true"><path d="M2 4h20v16H2zm2 2v.5l8 5.5 8-5.5V6zm0 3v9h16V9l-8 5.5z"/></svg></li>
      <li>www.corvantela.com.au
        <svg viewBox="0 0 24 24" aria-hidden="true"><path d="M12 2a10 10 0 1 0 0 20 10 10 0 0 0 0-20zm-1 17.9A8 8 0 0 1 4.1 9.6L9 14.5v1a2 2 0 0 0 2 2zm6.9-2.5A2 2 0 0 0 16 16h-1v-3a1 1 0 0 0-1-1H8v-2h2a1 1 0 0 0 1-1V7h2a2 2 0 0 0 2-2v-.4a8 8 0 0 1 2.9 12.8z"/></svg></li>
    </ul>
  </section>
</main>
</body>
</html>
```